Software Company Business Card

We are looking for a new design of our business card. The design will also be used in the rest of our branding and marketing materials as we want to keep it all uniform. We sell POS software to fine/luxury jewelers and also offer other business services as well to help the jeweler manage their business and need something more updated, technical and fresh, preferably more on the masculine side. We do not want any designs with gems in them but if possible would like to incorporate the circle and arrow in the logo into the design, but not a requirement if you can't make it work. I would like to see a variety of the mix. The colors need to remain our blue and orange and the logo can not change. The squiggly lines have been used as our corporate identity for over 20 years and its time to update. Our company name is PELK (Bright Ledger Counter Solutions).

Target Market(s)

High End Jewelers

Industry/Entity Type

Software

Contact Information for Business Card

Requirements
Must have
• Our logo and the colors must remain the same. Blue is #d95d39 and Orange is #0f5682.
Nice to have
• The circle and arrow incorporated but not a requirement.
Should not have
• Anything jewelry or gem related.

```html
<!DOCTYPE html>
<html lang="en">
<head>
<meta charset="utf-8">
<title>PELK Business Card</title>
<link href="https://fonts.googleapis.com/css2?family=Montserrat:wght@800&family=Arimo:wght@400&family=Lato:wght@400;700&display=swap" rel="stylesheet">
<style>
  :root {
    --brand-blue: #0f5682;
    --brand-orange: #d95d39;
    --paper: #ffffff;
    --ink: #1e1e1e;
    --backdrop: #e3dad9;
  }
  * { margin: 0; padding: 0; box-sizing: border-box; }
  html, body {
    width: 1200px; height: 801px; overflow: hidden;
    background: var(--backdrop);
  }
  .sheet { position: relative; width: 1200px; height: 801px; }
  .card {
    position: absolute; top: 274px;
    width: 443px; height: 263px; overflow: hidden;
  }
  .card--front { left: 153px; background: var(--paper); }
  .card--back { left: 625px; background: var(--brand-blue); }

  .front__band {
    position: absolute; left: 0; top: 0; width: 100%; height: 71px;
    background: var(--brand-blue);
  }
  .front__accent {
    position: absolute; right: 0; top: 0; width: 109px; height: 71px;
    background: var(--brand-orange);
  }
  .front__disc {
    position: absolute; left: 268px; top: 9px;
    width: 124px; height: 124px; border-radius: 50%;
    background: var(--brand-orange);
    border: 12px solid #f6f7f8;
  }
  .wordmark {
    position: absolute;
    font-family: "Montserrat", sans-serif; font-weight: 800;
    color: var(--paper); letter-spacing: -1px; line-height: 1;
  }
  .front__wordmark { left: 23px; top: 12px; font-size: 42px; }

  .address {
    position: absolute; left: 25px; top: 120px;
    font-family: "Arimo", sans-serif; font-size: 13px; line-height: 16px;
    color: var(--ink);
  }
  .contacts {
    position: absolute; left: 24px; top: 183px; list-style: none;
    font-family: "Arimo", sans-serif; font-size: 13px; color: var(--ink);
  }
  .contacts li { display: flex; align-items: center; height: 16.3px; }
  .contacts svg { width: 14px; height: 14px; margin-right: 4px; flex: none; }
  .contacts .domain { color: var(--brand-blue); }

  .person {
    position: absolute; right: 27px; top: 204px; text-align: right;
    font-family: "Lato", sans-serif;
  }
  .person__name { font-size: 20px; font-weight: 700; color: var(--brand-blue); line-height: 22px; }
  .person__role { font-size: 13px; font-weight: 400; color: var(--brand-orange); line-height: 16px; }

  .back__wordmark { left: 104px; top: 100px; font-size: 56px; }
  .back__disc {
    position: absolute; left: 289px; top: 107px;
    width: 50px; height: 50px; border-radius: 50%;
    background: var(--brand-orange);
  }
</style>
</head>
<body>
<main class="sheet">
  <section class="card card--front" aria-label="Card front">
    <div class="front__band"></div>
    <div class="front__accent"></div>
    <div class="front__disc"></div>
    <div class="wordmark front__wordmark">pelk</div>

    <p class="address">418 Meridian Park Drive Suite 210<br>Carvale, OR 97412,USA</p>

    <ul class="contacts">
      <li>
        <svg viewBox="0 0 14 14" aria-hidden="true"><circle cx="7" cy="7" r="7" fill="var(--brand-orange)"/><path d="M4.6 3.6l1.3 1.6-.7.9c.5 1 1.3 1.8 2.3 2.3l.9-.7 1.6 1.3-.8 1.2C6.6 10 4 7.4 3.6 4.4z" fill="#fff"/></svg>
        + 800 555-0147
      </li>
      <li>
        <svg viewBox="0 0 14 14" aria-hidden="true"><circle cx="7" cy="7" r="7" fill="var(--brand-orange)"/><rect x="4.5" y="3.2" width="5" height="2.3" fill="#fff"/><rect x="3.3" y="5.8" width="7.4" height="3.4" rx=".6" fill="#fff"/><rect x="4.5" y="8.6" width="5" height="2.4" fill="#fff" stroke="var(--brand-orange)" stroke-width=".6"/></svg>
        +1 541 555-0192
      </li>
      <li>
        <svg viewBox="0 0 14 14" aria-hidden="true"><circle cx="7" cy="7" r="7" fill="var(--brand-orange)"/><rect x="3.4" y="4.4" width="7.2" height="5.2" fill="#fff"/><path d="M3.6 4.6L7 7.4l3.4-2.8" fill="none" stroke="var(--brand-orange)" stroke-width=".8"/></svg>
        dorian@pelkusa.com
      </li>
      <li>
        <svg viewBox="0 0 14 14" aria-hidden="true"><circle cx="7" cy="7" r="7" fill="var(--brand-orange)"/><g fill="none" stroke="#fff" stroke-width=".8"><circle cx="7" cy="7" r="3.6"/><ellipse cx="7" cy="7" rx="1.6" ry="3.6"/><path d="M3.4 7h7.2M3.9 5.3h6.2M3.9 8.7h6.2"/></g></svg>
        www.<span class="domain">pelkusa</span>.com
      </li>
    </ul>

    <div class="person">
      <p class="person__name">Dorian Keswick</p>
      <p class="person__role">Director of Global Operations</p>
    </div>
  </section>

  <section class="card card--back" aria-label="Card back">
    <div class="wordmark back__wordmark">pelk</div>
    <div class="back__disc"></div>
  </section>
</main>
</body>
</html>
```